Varnel Supply requires a new business card.

We are an online professional tool store.

Target Market(s)

We target the professional technician.

Industry/Entity Type

Business

Contact Information for Business Card

VarnelSupply.com.au

sales@varnelsupply.example

Requirements
Must have
• Needs to look commercial and professional
Should not have
• No Australian Colors, maps or shapes.
• No Shapes of Tools

```html
<!DOCTYPE html>
<html lang="en">
<head>
<meta charset="utf-8">
<title>Varnel Supply – Business Card</title>
<link href="https://fonts.googleapis.com/css2?family=Roboto:wght@500;700&display=swap" rel="stylesheet">
<style>
  :root {
    --backdrop: #d3d1d2;
    --card-white: #ffffff;
    --brand-navy: #2d4397;
    --text-navy: #2d3a8c;
    --accent-cyan: #1a9bd1;
    --text-light: #ffffff;
  }
  * { margin: 0; padding: 0; box-sizing: border-box; }
  html, body {
    width: 1200px;
    height: 1200px;
    overflow: hidden;
    background: var(--backdrop);
    font-family: "Roboto", Arial, sans-serif;
  }
  .canvas {
    position: relative;
    width: 1200px;
    height: 1200px;
  }
  .card {
    position: absolute;
    border-radius: 6px;
    display: flex;
    flex-direction: column;
    align-items: center;
  }
  .card--front {
    left: 392px;
    top: 62px;
    width: 365px;
    height: 640px;
    background: var(--card-white);
  }
  .card--back {
    left: 234px;
    top: 738px;
    width: 679px;
    height: 389px;
    background: var(--brand-navy);
  }
  .brand {
    display: flex;
    flex-direction: column;
    align-items: center;
    position: absolute;
    left: 50%;
    transform: translateX(-50%);
    white-space: nowrap;
  }
  .brand__dot {
    border-radius: 50%;
    background: var(--accent-cyan);
    flex: none;
  }
  .brand__name {
    font-weight: 700;
    line-height: 1;
  }
  .card--front .brand { top: 48px; gap: 22px; }
  .card--front .brand__dot { width: 140px; height: 140px; }
  .card--front .brand__name { font-size: 46px; color: var(--text-navy); }

  .card--back .brand { top: 72px; gap: 22px; }
  .card--back .brand__dot { width: 150px; height: 150px; }
  .card--back .brand__name { font-size: 60px; color: var(--text-light); }

  .contact-icons {
    position: absolute;
    top: 416px;
    display: flex;
    gap: 8px;
  }
  .contact-icons svg { width: 36px; height: 36px; display: block; }

  .contact-list {
    position: absolute;
    top: 468px;
    list-style: none;
    text-align: center;
    color: var(--text-navy);
    font-weight: 700;
    font-size: 21px;
    line-height: 32px;
  }
  .web-address {
    position: absolute;
    top: 344px;
    color: var(--text-light);
    font-weight: 500;
    font-size: 23px;
  }
</style>
</head>
<body>
<main class="canvas">
  <section class="card card--front">
    <div class="brand">
      <span class="brand__dot"></span>
      <span class="brand__name">Varnel Supply</span>
    </div>

    <div class="contact-icons">
      <svg viewBox="0 0 36 36" aria-label="Website">
        <circle cx="18" cy="18" r="17" fill="var(--accent-cyan)"/>
        <circle cx="18" cy="18" r="13" fill="none" stroke="#fff" stroke-width="1.6"/>
        <circle cx="18" cy="18" r="9" fill="none" stroke="#fff" stroke-width="1.2"/>
        <ellipse cx="18" cy="18" rx="4" ry="9" fill="none" stroke="#fff" stroke-width="1.1"/>
        <line x1="9" y1="18" x2="27" y2="18" stroke="#fff" stroke-width="1.1"/>
        <line x1="10.5" y1="13.5" x2="25.5" y2="13.5" stroke="#fff" stroke-width="1"/>
        <line x1="10.5" y1="22.5" x2="25.5" y2="22.5" stroke="#fff" stroke-width="1"/>
      </svg>
      <svg viewBox="0 0 36 36" aria-label="Email">
        <circle cx="18" cy="18" r="17" fill="var(--accent-cyan)"/>
        <circle cx="18" cy="18" r="13" fill="none" stroke="#fff" stroke-width="1.6"/>
        <rect x="11" y="13" width="14" height="10" rx="1.5" fill="#fff"/>
        <polyline points="11.5,13.8 18,18.6 24.5,13.8" fill="none" stroke="var(--accent-cyan)" stroke-width="1.4"/>
      </svg>
    </div>

    <ul class="contact-list">
      <li class="contact-list__web">VarnelSupply.com.au</li>
      <li class="contact-list__email">sales@varnelsupply.example</li>
    </ul>
  </section>

  <section class="card card--back">
    <div class="brand">
      <span class="brand__dot"></span>
      <span class="brand__name">Varnel Supply</span>
    </div>
    <p class="web-address">VarnelSupply.com.au</p>
  </section>
</main>
</body>
</html>
```